Gestaltung eines Merkblattes
Ein Entwurf, der genau meinen Vorstellungen entspricht. Eine Abwicklung, die schneller und professioneller nicht sein könnte. Die Kommunikation - sehr symphatisch und kundenorientiert. Resumee: Besser geht es nicht.
Zielgruppe
www.tierklang-analytik.de/ Medizinische Bioresonanzanalysen für Pferde. Die Kundschaft besteht hauptsächlich aus Frauen, Alter von 20- 55 Jahre.
Bei dem Projekt handelt es sich um die Gestaltung eines wichtigen Merkblattes, das jedem Kunde zusammen mit dem Befund der Analyse gemailt wird. Es enthält wichtige Informationen rund um die Bioresonanzanalyse und sollte als pdf- Datei vorliegen.
Aufgabenstellung
Kernproblem: Die Kunden lesen das Merkblatt gar nicht oder nicht sorgfältig. So entstehen viele Fragen in der Folge, die nicht notwendig wären.
Wir benötigen eine pdf- Datei, die zum Lesen anregt, gerne gelesen wird und in der die wichtigsten Aspekte in das Auge fallen. Diese wurden von mir in der Worddatei, die den Text enthält, rot markiert.
Der Text in schwarz ist deutlich weniger wichtig.
Ach ja, die Überschrift ist doof. 'Allgemeine Hinweise' das animiert nicht wirklich zum Lesen. Falls Sie eine griffige Idee haben, sehr gerne.

```html
<!DOCTYPE html>
<html lang="de">
<head>
<meta charset="utf-8">
<title>Merkblatt – Tierklang Analytik</title>
<link href="https://fonts.googleapis.com/css2?family=Oswald:wght@300;400&family=Fira+Sans+Extra+Condensed:wght@300;400&display=swap" rel="stylesheet">
<style>
  :root {
    --green: #bcc274;
    --green-text: #b2b865;
    --ink: #4a4a4a;
    --title: #555555;
    --paper: #ffffff;
  }
  * { box-sizing: border-box; margin: 0; padding: 0; }
  html, body { width: 848px; height: 1200px; overflow: hidden; background: var(--paper); }
  .sheet { position: relative; width: 848px; height: 1200px; overflow: hidden; }

  .top-band { position: absolute; left: 273px; top: 27px; width: 575px; height: 19px; background: var(--green); }

  .brand { position: absolute; left: 25px; top: 72px; display: flex; align-items: center; gap: 8px; }
  .brand-dot { width: 20px; height: 20px; border-radius: 50%; background: var(--green); }
  .brand-name { font-family: "Oswald", sans-serif; font-weight: 400; font-size: 26px; color: var(--green-text); letter-spacing: 0.4px; }

  .page-title { position: absolute; left: 274px; top: 61px; font-family: "Oswald", sans-serif; font-weight: 300; font-size: 31px; line-height: 40px; color: var(--title); white-space: nowrap; }

  .section-title, .topic-title { position: absolute; font-family: "Oswald", sans-serif; font-weight: 300; color: var(--green-text); white-space: nowrap; }
  .section-title { left: 101px; font-size: 24.5px; line-height: 30px; }
  .topic-title { font-size: 20px; line-height: 24px; }

  .topic-text { position: absolute; width: 186px; font-family: "Fira Sans Extra Condensed", sans-serif; font-weight: 300; font-size: 16px; line-height: 18.8px; color: var(--ink); }
  .topic-text p + p { margin-top: 7px; }
  .ln { display: block; white-space: nowrap; text-align: justify; text-align-last: justify; }
  .ln.end { text-align-last: left; }

  .c1 { left: 103px; } .c2 { left: 329px; } .c3 { left: 555px; }

  .illustration { position: absolute; background: linear-gradient(160deg, #e6e8c8, #d2d59c); border-radius: 6px; }
</style>
</head>
<body>
<div class="sheet">
  <div class="top-band"></div>

  <div class="brand">
    <span class="brand-dot"></span>
    <span class="brand-name">Tierklang Analytik</span>
  </div>

  <h1 class="page-title">BITTE ZUM WOHLE IHRES PFERDES LESEN!</h1>

  <!-- Befund -->
  <h2 class="section-title" style="top:181px">WAS SIE ZUM BEFUND DER ANALYSE WISSEN SOLLTEN</h2>
  <h3 class="topic-title c1" style="top:219px;left:101px">MEDIKAMENTENGABE</h3>
  <h3 class="topic-title c2" style="top:219px;left:327px">KEINE UNTERBRECHUNGEN</h3>
  <h3 class="topic-title c3" style="top:219px;left:553px">FÜR WÄHLERISCHE PFERDE</h3>

  <div class="topic-text c1" style="top:262px">
    <p>
      <span class="ln">Die empfohlenen Präparate</span>
      <span class="ln">können (wenn nicht anders</span>
      <span class="ln">angegeben) in das normale</span>
      <span class="ln">Kraftfutter gegeben werden.</span>
      <span class="ln">Tropfen und Bachblüten bitte</span>
      <span class="ln">auf ein kleines Stück trocke-</span>
      <span class="ln">nes Brot, Zwieback, bei Pfer-</span>
      <span class="ln">den, die kein Getreide fressen</span>
      <span class="ln">dürfen, auf ein Stück Reis-</span>
      <span class="ln">waffel geben, und dem Pferd</span>
      <span class="ln end">direkt füttern.</span>
    </p>
    <p>
      <span class="ln">Vitabasis Pulver muss nicht,</span>
      <span class="ln">wie vom Hersteller angege-</span>
      <span class="ln">ben, in Wasser aufgelöst</span>
      <span class="ln">werden. Eine Gabe in das</span>
      <span class="ln">Kraftfutter, Heucobs etc. ver-</span>
      <span class="ln end">mindert nicht die Wirkung.</span>
    </p>
  </div>
  <div class="topic-text c2" style="top:262px">
    <p>
      <span class="ln">Bitte füttern Sie alle Präpara-</span>
      <span class="ln">te, außer es sind abweichen-</span>
      <span class="ln">de Empfehlungen vorhan-</span>
      <span class="ln">den, ohne Unterbrechung,</span>
      <span class="ln">bis Ihnen das Ergebnis der</span>
      <span class="ln end">ersten Nachtestung vorliegt.</span>
    </p>
    <p>
      <span class="ln">Pausen von mehr als zwei</span>
      <span class="ln">Tagen können zu Beginn der</span>
      <span class="ln">Behandlung die positive Ent-</span>
      <span class="ln">wicklung Ihres Pferdes beein-</span>
      <span class="ln end">trächtigen.</span>
    </p>
  </div>
  <div class="illustration" style="left:368px;top:478px;width:100px;height:94px" role="img" aria-label="Linienzeichnung einer Hand, die Futterpellets streut"></div>
  <div class="topic-text c3" style="top:262px">
    <p>
      <span class="ln">Falls Ihr Pferd sehr wählerisch</span>
      <span class="ln">ist bei der Zufütterung von</span>
      <span class="ln">Präparaten in Pellets- oder</span>
      <span class="ln">Pulverform, dann beginnen</span>
      <span class="ln">Sie mit einer sehr kleinen</span>
      <span class="ln">Dosierung von z. b. ½ Tee-</span>
      <span class="ln">löffel und steigern diese sehr</span>
      <span class="ln end">langsam.</span>
    </p>
    <p>
      <span class="ln">Bei trockenem Futter (Müsli,</span>
      <span class="ln">Hafer) sortieren manche</span>
      <span class="ln">Pferde gerne aus. Hier ist</span>
      <span class="ln">es sinnvoll, das Futter anzu</span>
      <span class="ln">feuchten, etwas Heucobs</span>
      <span class="ln">oder getreidefreies Mash da-</span>
      <span class="ln end">zuzugeben.</span>
    </p>
  </div>

  <!-- Nachtestung -->
  <h2 class="section-title" style="top:617px">WAS SIE ZUR NACHTESTUNG WISSEN SOLLTEN</h2>
  <h3 class="topic-title" style="top:655px;left:101px">HAARPROBE UND FEEDBACK</h3>
  <h3 class="topic-title" style="top:655px;left:327px">KEINE EINGANGSBESTÄTIGUNG</h3>
  <h3 class="topic-title" style="top:655px;left:553px">ERGEBNIS PER MAIL</h3>

  <div class="topic-text c1" style="top:687px">
    <p>
      <span class="ln">Wir brauchen für die Nach-</span>
      <span class="ln">testung eine neue Haarpro-</span>
      <span class="ln">be und ein kurzes Feedback</span>
      <span class="ln">zu der aktuellen Entwicklung</span>
      <span class="ln end">Ihres Pferdes. Mehr nicht.</span>
    </p>
  </div>
  <div class="topic-text c2" style="top:687px">
    <p>
      <span class="ln">Wir bestätigen den Eingang</span>
      <span class="ln">der Probe zur Nachtestung</span>
      <span class="ln">nicht. In regelmäßigen Ab-</span>
      <span class="ln">ständen werden alle Befun-</span>
      <span class="ln end">de nachgetestet.</span>
    </p>
  </div>
  <div class="topic-text c3" style="top:687px">
    <p>
      <span class="ln">Wir senden Ihnen im An-</span>
      <span class="ln">schluss per Mail das neue Er-</span>
      <span class="ln">gebnis mit einer aktualisier-</span>
      <span class="ln end">ten Therapieempfehlung zu.</span>
    </p>
  </div>

  <!-- Bachblüten -->
  <h2 class="section-title" style="top:809px">WAS SIE ZUR BACHBLÜTEN-THERAPIE WISSEN SOLLTEN</h2>
  <h3 class="topic-title" style="top:848px;left:101px">BACHBLÜTEN</h3>
  <h3 class="topic-title" style="top:848px;left:327px">SEELISCHER ZUSTAND</h3>
  <h3 class="topic-title" style="top:848px;left:553px">HERSTELLUNG</h3>

  <div class="topic-text c1" style="top:888px">
    <p>
      <span class="ln">Wenn die Therapieempfeh-</span>
      <span class="ln">lung eine Übersicht an Bach-</span>
      <span class="ln">blüten enthält, dann spie-</span>
      <span class="ln">geln diese den seelischen</span>
      <span class="ln">Zustand Ihres Pferdes wieder,</span>
      <span class="ln">der von seinen aktuellen Le-</span>
      <span class="ln">bensbedingungen, seiner</span>
      <span class="ln">körperlichen Belastung durch</span>
      <span class="ln">Krankheit und durch Abläu-</span>
      <span class="ln">fe in seiner Herde beeinflusst</span>
      <span class="ln end">wird.</span>
    </p>
  </div>
  <div class="illustration" style="left:203px;top:1100px;width:66px;height:66px" role="img" aria-label="Linienzeichnung einer Pipette mit fallendem Tropfen"></div>
  <div class="topic-text c2" style="top:888px">
    <p>
      <span class="ln">Erfahrungsgemäß bezieht</span>
      <span class="ln">sich die Darstellung der</span>
      <span class="ln">Blüten bei Pferden, die in</span>
      <span class="ln">einer Herde leben, häufig</span>
      <span class="ln">mehr auf die Gefühle des</span>
      <span class="ln">Pferdes gegenüber seinen</span>
      <span class="ln">Artgenossen als auf den Kon-</span>
      <span class="ln end">takt mit dem Menschen.</span>
    </p>
    <p>
      <span class="ln">Die meisten Apotheken</span>
      <span class="ln">kennen sich aus mit der Her-</span>
      <span class="ln">stellung einer Bachblütenmi-</span>
      <span class="ln">schung. Falls nicht, hier die</span>
      <span class="ln end">Anleitung:</span>
    </p>
  </div>
  <div class="topic-text c3" style="top:888px">
    <p>
      <span class="ln">In ein 30 ml Medizinfläsch-</span>
      <span class="ln">chen mit Tropfvorrichtung</span>
      <span class="ln">oder Pipette gibt man 10 ml</span>
      <span class="ln">Alkohol (Brandy oder Wein-</span>
      <span class="ln">brand), 20 ml Quellwasser</span>
      <span class="ln">oder stilles Mineralwasser</span>
      <span class="ln">(ohne Kohlensäure; kein</span>
      <span class="ln">destilliertes Wasser!) und 2-3</span>
      <span class="ln">Tropfen von jeder Blüte, die</span>
      <span class="ln">im Moment benötigt wird.</span>
      <span class="ln">Als Alternative zu Alkohol</span>
      <span class="ln">kann auch Obstessig einge-</span>
      <span class="ln end">setzt werden.</span>
    </p>
  </div>
</div>
</body>
</html>
```